HPS business cards

(Generators . Lighting Towers . De-watering Pumps . Compressors) put under the logo please. my details are Owen Pritchard (Director) 0461527390 harbourpinesupply@postvale.net

```html
<!DOCTYPE html>
<html lang="en">
<head>
<meta charset="utf-8">
<title>HPS business cards</title>
<link href="https://fonts.googleapis.com/css2?family=Michroma&family=Lato:wght@400&display=swap" rel="stylesheet">
<style>
  :root {
    --backdrop: #1c1c1e;
    --card: #111112;
    --card-edge: #242426;
    --gold: #f0a81e;
    --gold-soft: #c98a1a;
    --silver: #d9d9dc;
    --text-light: #e6e6e6;
    --pattern-dark: #151516;
    --pattern-light: #2a2a2c;
  }
  * { margin: 0; padding: 0; box-sizing: border-box; }
  html, body {
    width: 1200px; height: 800px; overflow: hidden;
    background: var(--backdrop);
  }
  .canvas {
    position: relative; width: 1200px; height: 800px;
    display: flex; align-items: center; justify-content: center; gap: 50px;
  }
  .card {
    position: relative; width: 540px; height: 310px;
    background: var(--card);
    border-radius: 16px;
    border: 1px solid var(--card-edge);
    overflow: hidden;
    box-shadow: 0 18px 40px rgba(0,0,0,.55);
  }

  /* front */
  .card-front .brand-mark {
    position: absolute; left: 30px; top: 0; width: 190px; height: 100%;
    display: flex; align-items: center; justify-content: center;
    font-family: "Michroma", sans-serif; font-size: 48px; color: var(--gold);
    letter-spacing: 2px;
  }
  .card-front .divider {
    position: absolute; left: 244px; top: 112px; width: 1px; height: 86px;
    background: var(--gold-soft);
  }
  .card-front .details {
    position: absolute; left: 266px; top: 96px; right: 16px;
    font-family: "Lato", sans-serif; color: var(--text-light);
  }
  .details .name {
    font-family: "Michroma", sans-serif; font-size: 15px; color: var(--gold);
    text-transform: uppercase; letter-spacing: .5px; line-height: 1.1;
    white-space: nowrap;
  }
  .details .role { font-size: 13px; margin: 5px 0 14px; }
  .contact { list-style: none; }
  .contact li {
    display: flex; align-items: center; gap: 8px;
    font-size: 11.5px; line-height: 1; margin-bottom: 9px; white-space: nowrap;
  }
  .contact svg { width: 11px; height: 11px; flex: none; }

  /* back */
  .card-back .pattern-area {
    position: absolute; inset: 0;
    background: linear-gradient(120deg, var(--pattern-light) 0%, var(--pattern-dark) 55%, #0d0d0e 100%);
  }
  .card-back .brand-lockup {
    position: absolute; inset: 0;
    display: flex; flex-direction: column; align-items: center; justify-content: center;
    font-family: "Michroma", sans-serif; color: var(--gold); text-align: center;
  }
  .brand-lockup .initials { font-size: 60px; letter-spacing: 4px; line-height: 1; }
  .brand-lockup .full-name { font-size: 21px; letter-spacing: 3px; margin-top: 16px; }
  .brand-lockup .services {
    margin-top: 14px;
    font-family: "Lato", sans-serif; font-size: 11.5px; letter-spacing: .4px;
    color: var(--silver); white-space: nowrap;
  }
</style>
</head>
<body>
<main class="canvas">

  <section class="card card-front" aria-label="Card front">
    <div class="brand-mark">HPS</div>
    <div class="divider"></div>
    <div class="details">
      <p class="name">Owen Pritchard</p>
      <p class="role">Director</p>
      <ul class="contact">
        <li>
          <svg viewBox="0 0 12 12" aria-hidden="true"><path d="M3 1 L5 3.5 L3.8 4.8 C4.6 6.4 5.6 7.4 7.2 8.2 L8.5 7 L11 9 L9.6 11 C5.5 10.5 1.5 6.5 1 2.4 Z" fill="var(--gold)"/></svg>
          0461527390
        </li>
        <li>
          <svg viewBox="0 0 12 12" aria-hidden="true"><rect x="1" y="2.5" width="10" height="7" fill="var(--gold)"/><path d="M1 2.5 L6 6.5 L11 2.5" stroke="var(--card)" stroke-width="1" fill="none"/></svg>
          harbourpinesupply@postvale.net
        </li>
        <li>
          <svg viewBox="0 0 12 12" aria-hidden="true"><circle cx="6" cy="6" r="5" fill="none" stroke="var(--gold)" stroke-width="1.4"/><path d="M1 6 H11 M6 1 C3.5 4 3.5 8 6 11 M6 1 C8.5 4 8.5 8 6 11" stroke="var(--gold)" stroke-width=".9" fill="none"/></svg>
          harbourpinesupply.net
        </li>
      </ul>
    </div>
  </section>

  <section class="card card-back" aria-label="Card back">
    <div class="pattern-area" role="img" aria-label="Repeating tone-on-tone brand pattern in spot gloss across the card"></div>
    <div class="brand-lockup">
      <span class="initials">HPS</span>
      <span class="full-name">HARBOUR PINE SUPPLY</span>
      <span class="services">(Generators . Lighting Towers . De-watering Pumps . Compressors)</span>
    </div>
  </section>

</main>
</body>
</html>
```